Flyer needed to promote gutter clearance service for established gardening company

We need a bright and engaging flyer to be designed to advertise our gutter clearance service.
Whilst we are a gardening company that normally does more horticultural work, during the winter we offer other services such as gutter clearance where we remove the debris from gutters and thereby reducing the risk of clogs, leakage, breakage and potential structural damage to the property.

Full details of our service, together with our overall brand and colours can be seen on www.hartleyoutdoorcare.co.uk/gutters.

We would like you to use the page on the website as a basis to create the flyer and so please feel free to use as much or as little of the wording contained within the webpage on the flyer drawing particular attention to "Prices starting at just £60 for an average 3 bed house". I will upload pictures but please feel free to use other graphics and fonts to make it stand out.

The contact details which should be included within the flyer are as follows:

Hartley Outdoor Care Ltd
Kestrel Trade Park
Whitlow Moor Ind Estate
Swindon
SN3 7QL

Tel: 01793 418203
www.hartleyoutdoorcare.co.uk
mark@hartleyoutdoorcare.co.uk

The flyers will eventually be printed out in A5 (210mm x 148mm) using Printaloft and so needs to be in that size and suitable file for upload.

I have only put this as a 2 day project as its really urgent and I'm hoping we get some great designs in that time.

Target Market(s)

Homeowners between 25 - 65+

Industry/Entity Type

Home Improvement

Font styles to use
Serif
Sans Serif
Decorative
Script

Colors
6b449b
9bcb3c

Requirements
Must have
• Our colours are purple and green as seen on our website www.hartleyoutdoorcare.co.uk/gutters. Please use those colours.
• The flyer should draw attention to the following facts:
• We are Hartley Outdoor Care Ltd (see attached logo)
• We are offering a Gutter Clearance Service in Swindon
• Prices start at just £60 for the average 3 bed house.
• We are fully insured.
• Our contact details must be included (as in the product description above)
• I have attached pictures but feel free to add other graphics or use fonts to make the flyer more engaging and interesting.
• Additional wording may be taken from the website at the address shown above. You can use as much or as little wording as you like just as long as the message gets across and the flyer contains our contact information and logo and the details shown above.
Nice to have
• I would like a bright and modern design which isn't too busy or cluttered. It should be something that is quick and easy to read.
Should not have
• I don't want it to look too busy or crowded with small type which people just won't read. Whilst I've said you can take whatever wording you want from our website, I'd suggest you don't take it all or too much. I want the main message (as detailed above in 'must haves') to stand out rather than have it contained deep within lots of small type face.

```html
<!DOCTYPE html>
<html lang="en">
<head>
<meta charset="utf-8">
<title>Hartley Outdoor Care – Gutter Clearance Flyer</title>
<link href="https://fonts.googleapis.com/css2?family=Roboto+Condensed:ital,wght@0,400;0,700;1,700&family=Roboto:wght@400;700;900&display=swap" rel="stylesheet">
<style>
  :root{
    --green:#3fae49;
    --green-dark:#2f9a3a;
    --brown:#3b2518;
    --ink:#2b1c14;
    --white:#ffffff;
    --page:#e9e6e2;
  }
  *{box-sizing:border-box;margin:0;padding:0}
  html,body{width:1200px;height:1200px;overflow:hidden;background:var(--page)}
  body{position:relative;font-family:"Roboto Condensed",sans-serif;color:var(--ink)}

  .flyer{position:absolute;background:var(--white);overflow:hidden;box-shadow:0 4px 14px rgba(0,0,0,.18)}
  .front{left:64px;top:72px;width:544px;height:788px}
  .back{left:628px;top:346px;width:544px;height:770px}

  .brand{position:absolute;display:flex;align-items:center;gap:8px;font-family:"Roboto Condensed",sans-serif;font-weight:700;color:var(--brown)}
  .brand-dot{width:14px;height:14px;border-radius:50%;background:var(--green)}
  .front .brand{left:0;right:0;top:70px;justify-content:center;font-size:34px}

  .headline{position:absolute;left:0;right:0;top:150px;text-align:center;font-size:28px;color:var(--ink)}
  .headline strong{font-size:42px;font-weight:400;letter-spacing:.5px}
  .sub{position:absolute;left:0;right:0;top:200px;text-align:center;font-family:"Roboto",sans-serif;font-size:15px}
  .service{position:absolute;left:0;right:0;top:228px;text-align:center;font-size:37px;color:var(--green);letter-spacing:.3px}

  .roof-photo{position:absolute;left:0;top:270px;width:544px;height:430px;
    background:linear-gradient(180deg,#ffffff 0%,#e8ebee 22%,#a9adb2 48%,#6d6a66 72%,#8f8a80 100%)}
  .before-after{position:absolute;left:48px;top:293px;width:204px;height:183px;border:4px solid #222;border-radius:4px;display:flex;background:#222;gap:2px}
  .before-after div{flex:1;position:relative}
  .before-after .before{background:linear-gradient(180deg,#6b5a3f,#8a7040 60%,#4f6b3a)}
  .before-after .after{background:linear-gradient(180deg,#8a8f88,#c9cbc4 60%,#6f8a55)}
  .before-after span{position:absolute;top:4px;left:0;right:0;text-align:center;font-family:"Roboto",sans-serif;font-weight:700;font-size:12px;color:var(--white)}

  .price{position:absolute;left:268px;width:250px;top:288px;text-align:center;font-family:"Roboto",sans-serif;color:var(--ink)}
  .price-lead{font-size:27px}
  .price-amount{font-weight:900;font-size:82px;line-height:1;color:var(--green);margin-top:4px}
  .price-tail{font-size:27px;line-height:1.2;margin-top:2px;text-shadow:0 0 6px #fff,0 0 10px #fff}
  .insured{position:absolute;left:90px;top:487px;font-family:"Roboto",sans-serif;font-weight:700;font-size:20px;color:var(--white)}

  .front-wave{position:absolute;left:0;top:540px;width:544px;height:160px}
  .front-contact{position:absolute;left:0;right:0;top:650px;text-align:center}
  .company{font-family:"Roboto",sans-serif;font-weight:700;font-size:18px;color:#3d2b6e}
  .address{font-size:15px;color:#3d2b6e;margin-top:2px}
  .front-footer{position:absolute;left:0;right:0;top:694px;height:94px;background:var(--brown);color:var(--white);text-align:center;font-family:"Roboto",sans-serif}
  .front-footer .tel{font-size:18px;margin-top:12px}
  .front-footer .web{font-size:12px;letter-spacing:5px;margin-top:12px}

  .photo{position:absolute}
  .p-vacuum{left:0;top:0;width:192px;height:220px;background:linear-gradient(135deg,#b85a3a,#d9c9a8 55%,#3a3a3a)}
  .p-scoop{left:194px;top:0;width:350px;height:220px;background:linear-gradient(160deg,#d8d8d6,#6c8a3a 55%,#5a4a38)}
  .p-family{left:0;top:222px;width:230px;height:270px;background:linear-gradient(180deg,#3f78c4 0%,#9a4a3c 45%,#c7c3bb 70%,#5f8f3a 100%)}
  .p-leaves{left:233px;top:222px;width:311px;height:230px;background:linear-gradient(150deg,#9aa04a,#5f6268 45%,#c9a24a 75%,#2aa6a0)}
  .back-brand{position:absolute;left:178px;top:157px;width:214px;height:112px;background:var(--white);display:flex;align-items:center;justify-content:center;gap:7px;font-weight:700;font-size:24px;color:var(--brown)}
  .back-shapes{position:absolute;left:0;top:0;width:544px;height:770px}
  .help{position:absolute;right:42px;top:436px;text-align:right;color:var(--white)}
  .help h2{font-weight:400;font-size:28px}
  .help p{font-size:15px;line-height:1.3;margin-top:6px}
  .about{position:absolute;left:22px;right:38px;top:552px;color:var(--white)}
  .about h3{font-weight:400;font-size:20px}
  .about p{font-size:14.5px;line-height:1.28;margin-top:2px;color:#1f1a14}
  .call{position:absolute;left:24px;top:662px;color:var(--white);font-size:17px;display:flex;align-items:baseline;gap:6px}
  .call strong{font-style:italic;font-weight:700;font-size:36px;color:var(--brown)}
  .back-web{position:absolute;left:0;right:0;top:722px;text-align:center;font-family:"Roboto",sans-serif;font-size:20px;letter-spacing:4px;color:var(--ink)}
</style>
</head>
<body>

<article class="flyer front">
  <div class="brand"><span class="brand-dot"></span>Hartley Outdoor Care</div>
  <h1 class="headline">As the <strong>SEASONS CHANGE</strong></h1>
  <p class="sub">we offer a wide range of supplementary seasonal services.</p>
  <h2 class="service">GUTTER CLEARANCE SERVICES</h2>

  <div class="roof-photo" role="img" aria-label="Photo of a roof edge with hailstones and a gutter carrying water"></div>
  <div class="before-after">
    <div class="before" role="img" aria-label="Gutter full of leaves before clearing"><span>Before</span></div>
    <div class="after" role="img" aria-label="Clean gutter after clearing"><span>After</span></div>
  </div>

  <div class="price">
    <div class="price-lead">Prices start at just</div>
    <div class="price-amount">£60</div>
    <div class="price-tail">for the average<br>3 bed house.</div>
  </div>
  <div class="insured">*fully insured</div>

  <svg class="front-wave" viewBox="0 0 544 160" preserveAspectRatio="none" aria-hidden="true">
    <path d="M0 28 Q272 125 544 0 L544 160 L0 160 Z" fill="var(--green)"/>
  </svg>
  <div class="front-contact">
    <div class="company">Hartley Outdoor Care Ltd</div>
    <div class="address">Kestrel Trade Park Whitlow Moor Ind Estate Swindon SN3 7QL</div>
  </div>
  <footer class="front-footer">
    <div class="tel">Tel: 01793 418203 | mark@hartleyoutdoorcare.co.uk</div>
    <div class="web">www.hartleyoutdoorcare.co.uk</div>
  </footer>
</article>

<article class="flyer back">
  <div class="photo p-vacuum" role="img" aria-label="Worker using a gutter vacuum pipe"></div>
  <div class="photo p-scoop" role="img" aria-label="Gloved hand scooping moss from a gutter"></div>
  <div class="photo p-family" role="img" aria-label="Family standing in front of their house"></div>
  <div class="photo p-leaves" role="img" aria-label="Gloved hands removing autumn leaves from roof gutter"></div>
  <div class="back-brand"><span class="brand-dot"></span>Hartley Outdoor Care</div>

  <svg class="back-shapes" viewBox="0 0 544 770" aria-hidden="true">
    <polygon points="0,482 544,405 544,562 0,482" fill="var(--brown)"/>
    <polygon points="0,482 544,562 544,705 0,705" fill="var(--green)"/>
    <rect x="0" y="705" width="544" height="5" fill="var(--brown)"/>
  </svg>

  <div class="help">
    <h2>How can we help?</h2>
    <p>Clearing gutters is not just a dirty job but<br>it can be a dangerous one too if not done properly.</p>
  </div>
  <div class="about">
    <h3>At Hartley Outdoor Care,</h3>
    <p>we are fully insured and use the latest tools and techniques to safely clear your gutters, giving you peace of mind without having to risk getting dirty or injured yourself. And with prices starting at just £60 to clear the gutters of an average 3 bed house, it is an affordable way to get your home prepared for the winter.</p>
  </div>
  <div class="call">Call Hartley Outdoor Care Ltd on <strong>01793 418203</strong></div>
  <div class="back-web">www.hartleyoutdoorcare.co.uk</div>
</article>

</body>
</html>
```